Construction Company

Design a clutter free business card, it can be double-sided utilizing the logo for BDN Ltd simple with all relevant contact information.

Please also a letterhead design to function for the purposes of invoicing, all mail requirements, with header to be distinctive while the footer ties page together and incorporates all necessary information.

For now, please use generic / dummy text and when a winner is selected, I will disclose the contact information.

Hi Designers! Please read the updated brief which includes the design of a business card and letterhead. Thank you!

```html
<!DOCTYPE html>
<html lang="en">
<head>
<meta charset="utf-8">
<title>BDN Ltd Business Card</title>
<link rel="stylesheet" href="https://fonts.googleapis.com/css2?family=Roboto:wght@400;500;700&display=swap">
<style>
  :root {
    --backdrop: #1f1f1f;
    --card-blue: #0a35a3;
    --card-blue-deep: #08308f;
    --gold: #c9a128;
    --white: #ffffff;
    --logo-blue: #3f8cff;
  }
  * { margin: 0; padding: 0; box-sizing: border-box; }
  html, body {
    width: 1200px;
    height: 800px;
    overflow: hidden;
    background: var(--backdrop);
    font-family: "Roboto", Arial, sans-serif;
  }
  .sheet {
    width: 1200px;
    height: 800px;
    display: flex;
    align-items: center;
    justify-content: center;
    gap: 40px;
  }
  .card {
    width: 520px;
    height: 300px;
    border-radius: 18px;
    background: var(--card-blue);
    position: relative;
    overflow: hidden;
  }
  /* Front */
  .card--front {
    display: flex;
    align-items: center;
    justify-content: center;
  }
  .brand {
    display: flex;
    align-items: center;
    gap: 14px;
  }
  .brand__dot {
    width: 34px;
    height: 34px;
    border-radius: 50%;
    background: var(--gold);
  }
  .brand__name {
    font-size: 52px;
    font-weight: 700;
    color: var(--logo-blue);
    letter-spacing: 1px;
  }
  /* Back */
  .contact {
    position: absolute;
    left: 44px;
    bottom: 34px;
    color: var(--white);
  }
  .contact__name {
    font-size: 17px;
    font-weight: 700;
    color: var(--gold);
    text-transform: uppercase;
    letter-spacing: 0.3px;
  }
  .contact__role {
    font-size: 11px;
    font-weight: 700;
    margin-top: 2px;
  }
  .contact__address {
    font-size: 10.5px;
    line-height: 1.4;
    margin-top: 12px;
  }
  .contact__lines {
    list-style: none;
    margin-top: 12px;
    font-size: 10.5px;
    line-height: 1.5;
  }
  .contact__lines li {
    display: flex;
    align-items: center;
    gap: 7px;
  }
  .contact__icon {
    width: 10px;
    height: 10px;
    fill: var(--gold);
    flex: none;
  }
</style>
</head>
<body>
<main class="sheet">
  <section class="card card--front" aria-label="Business card front">
    <div class="brand">
      <span class="brand__dot"></span>
      <span class="brand__name">BDN Ltd</span>
    </div>
  </section>

  <section class="card card--back" aria-label="Business card back">
    <div class="contact">
      <p class="contact__name">Daniel Reyes</p>
      <p class="contact__role">President</p>
      <p class="contact__address">4120 Cedar Ridge Road<br>Fairbanks, Alaska 99701</p>
      <ul class="contact__lines">
        <li>
          <svg class="contact__icon" viewBox="0 0 24 24" aria-hidden="true"><path d="M6.6 10.8a15.2 15.2 0 0 0 6.6 6.6l2.2-2.2c.3-.3.7-.4 1-.2 1.1.4 2.3.6 3.6.6.6 0 1 .4 1 1V20c0 .6-.4 1-1 1C10.6 21 3 13.4 3 4c0-.6.4-1 1-1h3.5c.6 0 1 .4 1 1 0 1.3.2 2.5.6 3.6.1.3 0 .7-.2 1z"/></svg>
          555-214-7730
        </li>
        <li>
          <svg class="contact__icon" viewBox="0 0 24 24" aria-hidden="true"><path d="M2 5h20v14H2z M2 5l10 7 10-7" /><path d="M3 6l9 6.3L21 6v1.5l-9 6.3-9-6.3z" fill="#0a35a3"/></svg>
          info@bdnltd.com
        </li>
        <li>
          <svg class="contact__icon" viewBox="0 0 24 24" aria-hidden="true"><circle cx="12" cy="12" r="10"/><path d="M2 12h20M12 2c3 3 3 17 0 20M12 2c-3 3-3 17 0 20" stroke="#0a35a3" stroke-width="1.6" fill="none"/></svg>
          www.bdnltd.com
        </li>
      </ul>
    </div>
  </section>
</main>
</body>
</html>
```